Business Card for a recruitment agency specializing in engineers and geeks.

I am looking to create Business Card Design for my company.
That
## Company name:
Quorvant Inc.
Quorvant is a term coined from the following concepts.
1. geek + engineer
2. geek utopia
## Company Description:
The concept of the company is to be a recruitment agency that creates a paradise for geeky engineers. We want to be a place where engineers can have more freedom and ideal career support.
# Target.
The noun itself is often given to companies that want to hire engineers, geeks, and IT-related personnel, so it would be nice to get the impression that this company seems to have good engineers and IT personnel. There are many occasions where I meet with the human resources department, president, or senior management and give it to them.
# Atmosphere
We are happy with simplicity, but with an impact that will help people remember the company. The logo is based on a dinosaur that does programming, so it should be somewhat playful, but since it will basically be used in a business setting, please don't make it too silly.
# About the logo
See the attached files. The company logo represents our engineers smiling upward because of our work, with the motif of a dinosaur doing programming.
## Color
We will leave the color scheme to you, but since the logo is in black and white, colors with such a taste would fit well.
## file format
ai, psd, png, svg
Industry/Entity Type
human resource and employment agency
Contact Information for Business Card
Company name, address, email, tel, URL,logo
Colors
Designer to choose colors to be used in the design.

```html
<!DOCTYPE html>
<html lang="en">
<head>
<meta charset="utf-8">
<title>Quorvant Inc. — Business Card</title>
<link rel="stylesheet" href="https://fonts.googleapis.com/css2?family=Roboto+Condensed:wght@300;700&family=Open+Sans:wght@400;600&display=swap">
<style>
  :root {
    --canvas: #e9e9e9;
    --card-dark: #1b1b1b;
    --card-light: #ffffff;
    --ink-dark: #2f3236;
    --ink-soft: #a8abb0;
    --ink-mid: #55595e;
    --rule: #c9cbce;
    --on-dark: #ffffff;
  }
  * { margin: 0; padding: 0; box-sizing: border-box; }
  html, body { width: 1200px; height: 900px; overflow: hidden; }
  body {
    background: var(--canvas);
    display: flex;
    flex-direction: column;
    align-items: center;
    justify-content: center;
    gap: 50px;
  }
  .card {
    width: 630px;
    height: 360px;
    position: relative;
    box-shadow: 0 10px 30px rgba(0,0,0,0.18);
  }
  /* Front */
  .card-front {
    background: var(--card-dark);
    color: var(--on-dark);
    display: flex;
    flex-direction: column;
    align-items: center;
    justify-content: center;
  }
  .brand {
    display: flex;
    flex-direction: column;
    align-items: center;
    gap: 12px;
    margin-top: -20px;
  }
  .brand-square {
    width: 30px;
    height: 30px;
    border: 2px solid var(--on-dark);
  }
  .brand-name {
    font-family: "Open Sans", sans-serif;
    font-weight: 600;
    font-size: 15px;
    letter-spacing: 0.5px;
  }
  .dots {
    position: absolute;
    bottom: 92px;
    left: 50%;
    transform: translateX(-50%);
    display: flex;
    gap: 7px;
  }
  .dots span {
    width: 4px; height: 4px; border-radius: 50%;
    background: var(--on-dark);
  }
  /* Back */
  .card-back {
    background: var(--card-light);
    display: flex;
    align-items: center;
    padding-left: 110px;
    padding-top: 50px;
  }
  .details {
    display: flex;
    align-items: flex-start;
  }
  .identity {
    font-family: "Roboto Condensed", sans-serif;
    text-align: right;
    padding-right: 16px;
    border-right: 1px solid var(--rule);
    line-height: 1;
  }
  .first-name {
    font-weight: 300;
    font-size: 40px;
    color: var(--ink-soft);
    letter-spacing: -0.5px;
  }
  .last-name {
    font-weight: 700;
    font-size: 42px;
    color: var(--ink-dark);
    letter-spacing: -0.5px;
    margin-top: 2px;
  }
  .designation {
    font-weight: 700;
    font-size: 10px;
    color: var(--ink-dark);
    letter-spacing: 0.5px;
    margin-top: 4px;
  }
  .contacts {
    list-style: none;
    padding-left: 14px;
    font-family: "Open Sans", sans-serif;
    font-size: 12px;
    color: var(--ink-mid);
  }
  .contacts li {
    display: flex;
    align-items: flex-start;
    gap: 10px;
    line-height: 17px;
  }
  .contacts svg { width: 11px; height: 11px; margin-top: 3px; flex: none; }
  .contacts .address span { display: block; }
</style>
</head>
<body>
  <section class="card card-front">
    <div class="brand">
      <div class="brand-square"></div>
      <div class="brand-name">Quorvant</div>
    </div>
    <div class="dots"><span></span><span></span><span></span></div>
  </section>

  <section class="card card-back">
    <div class="details">
      <div class="identity">
        <div class="first-name">FIRST NAME</div>
        <div class="last-name">LAST NAME</div>
        <div class="designation">DESIGNATION</div>
      </div>
      <ul class="contacts">
        <li>
          <svg viewBox="0 0 12 12"><path d="M3 1 L5 3.5 L4 5 Q5 7 7 8 L8.5 7 L11 9 L9.5 11 Q4 10 1 2.5 Z" fill="none" stroke="var(--ink-mid)" stroke-width="1.1"/></svg>
          1-555-472-0193
        </li>
        <li>
          <svg viewBox="0 0 12 12"><rect x="1" y="2.5" width="10" height="7" fill="none" stroke="var(--ink-mid)" stroke-width="1.1"/><path d="M1 2.5 L6 6.5 L11 2.5" fill="none" stroke="var(--ink-mid)" stroke-width="1.1"/></svg>
          hello@quorvant.com
        </li>
        <li>
          <svg viewBox="0 0 12 12"><circle cx="6" cy="6" r="5" fill="none" stroke="var(--ink-mid)" stroke-width="1.1"/><ellipse cx="6" cy="6" rx="2" ry="5" fill="none" stroke="var(--ink-mid)" stroke-width="1"/><path d="M1 6 H11" stroke="var(--ink-mid)" stroke-width="1"/></svg>
          www.quorvant.com
        </li>
        <li class="address">
          <svg viewBox="0 0 12 12"><path d="M6 11 Q2 6.5 2 4.5 A4 4 0 0 1 10 4.5 Q10 6.5 6 11 Z" fill="none" stroke="var(--ink-mid)" stroke-width="1.1"/><circle cx="6" cy="4.5" r="1.3" fill="var(--ink-mid)"/></svg>
          <div><span>12 Harbor Lane</span><span>Westbrook 4021.</span></div>
        </li>
      </ul>
    </div>
  </section>
</body>
</html>
```